Full service facility management

Stationery Branding needed for Envelopes, folders, letterheads to show the services we offer (valet, security, front desk/concierge, janitorial, maintenance services to CONDOMINIUMS). We need the our logo and colors to be branded to these items

Target Market(s)

Homeowner Condominiums / High Rise residential living

Font styles to use
Sans Serif

Colors
0355a3

```html
<!DOCTYPE html>
<html lang="en">
<head>
<meta charset="utf-8">
<title>Kestrel Group – Business Cards</title>
<link rel="stylesheet" href="https://fonts.googleapis.com/css2?family=Montserrat:wght@400;500;600;700;800&display=swap">
<style>
  :root {
    --brand-blue: #0355a3;
    --card-blue: #0b5bb0;
    --ink-gray: #4f4f52;
    --rule-gray: #5c5c60;
    --paper: #ffffff;
    --backdrop: #d6d5d2;
  }
  * { box-sizing: border-box; margin: 0; padding: 0; }
  html, body {
    width: 1200px; height: 801px; overflow: hidden;
    background: var(--backdrop);
    font-family: "Montserrat", sans-serif;
  }
  .stage {
    position: relative; width: 1200px; height: 801px;
    display: flex; align-items: center; justify-content: center; gap: 60px;
  }
  .card {
    width: 520px; height: 297px; position: relative;
    box-shadow: 0 6px 18px rgba(0,0,0,0.18);
  }

  /* Front card */
  .card-front { background: var(--paper); display: flex; align-items: center; }
  .brand-block {
    width: 250px; display: flex; flex-direction: column; align-items: center;
    padding-left: 20px;
  }
  .brand-square {
    width: 92px; height: 92px; border: 4px solid var(--rule-gray);
    margin-bottom: 12px;
  }
  .brand-name {
    font-weight: 700; color: var(--brand-blue); font-size: 24px;
    letter-spacing: 0.5px; white-space: nowrap;
  }
  .brand-tagline {
    font-weight: 600; color: var(--ink-gray); font-size: 10.5px;
    margin-top: 3px; white-space: nowrap;
  }
  .divider {
    width: 2px; height: 150px; background: var(--rule-gray); margin: 0 22px 0 14px;
  }
  .contact-block { color: var(--ink-gray); }
  .contact-name {
    font-weight: 700; color: var(--brand-blue); font-size: 16px; letter-spacing: 0.3px;
  }
  .contact-title { font-weight: 600; font-size: 12.5px; margin-bottom: 10px; }
  .contact-address { font-size: 11.5px; line-height: 1.45; margin-bottom: 4px; }
  .contact-line {
    display: flex; align-items: center; gap: 7px; font-size: 11.5px; line-height: 1.6;
  }
  .contact-icon { width: 12px; height: 12px; flex: none; }

  /* Back card */
  .card-back {
    background: linear-gradient(160deg, #0d63bd 0%, var(--card-blue) 55%, #08499a 100%);
    color: #fff; display: flex; flex-direction: column; align-items: center;
    justify-content: center; text-align: center;
  }
  .back-square {
    width: 96px; height: 96px; border: 4px solid #fff; margin-bottom: 12px;
  }
  .back-name { font-weight: 700; font-size: 34px; letter-spacing: 0.5px; line-height: 1; }
  .back-tagline { font-weight: 700; font-size: 13.5px; margin-top: 6px; }
  .service-list { margin-top: 12px; font-size: 13px; font-weight: 500; line-height: 1.45; }
  .service-list .dot { font-size: 10px; vertical-align: 2px; margin: 0 3px; }
</style>
</head>
<body>
<main class="stage">

  <section class="card card-front" aria-label="Business card front">
    <div class="brand-block">
      <div class="brand-square"></div>
      <div class="brand-name">KESTREL GROUP</div>
      <div class="brand-tagline">Facilities Management Services</div>
    </div>
    <div class="divider"></div>
    <div class="contact-block">
      <div class="contact-name">DANIEL MARLOWE</div>
      <div class="contact-title">Managing Director</div>
      <div class="contact-address">48 Harbour Vale Road,<br>Maplewood, ON L7R</div>
      <div class="contact-line">
        <svg class="contact-icon" viewBox="0 0 12 12"><path fill="#0355a3" d="M2.5 1 4.5 1 5.3 3.3 4 4.3C4.6 5.7 6.3 7.4 7.7 8L8.7 6.7 11 7.5 11 9.5C11 10.3 10.3 11 9.5 11 5 11 1 7 1 2.5 1 1.7 1.7 1 2.5 1Z"/></svg>
        <span>555.214.7730</span>
      </div>
      <div class="contact-line">
        <svg class="contact-icon" viewBox="0 0 12 12"><rect x="0.5" y="2" width="11" height="8" fill="#0355a3"/><path d="M1 2.6 6 6.6 11 2.6" stroke="#fff" fill="none" stroke-width="1"/></svg>
        <span>info@harborlineparking.net</span>
      </div>
      <div class="contact-line">
        <svg class="contact-icon" viewBox="0 0 12 12"><circle cx="6" cy="6" r="5.5" fill="#0355a3"/><ellipse cx="6" cy="6" rx="2.2" ry="5.5" fill="none" stroke="#fff" stroke-width="0.8"/><path d="M0.5 6H11.5" stroke="#fff" stroke-width="0.8"/></svg>
        <span>www.harborlineparking.net</span>
      </div>
    </div>
  </section>

  <section class="card card-back" aria-label="Business card back">
    <div class="back-square"></div>
    <div class="back-name">KESTREL GROUP</div>
    <div class="back-tagline">Facilities Management Services</div>
    <div class="service-list">
      <div><span class="dot">●</span>Valet <span class="dot">●</span>Security <span class="dot">●</span>Front desk/concierge <span class="dot">●</span>Janitorial</div>
      <div><span class="dot">●</span>Maintenance services to CONDOMINIUMS</div>
    </div>
  </section>

</main>
</body>
</html>
```